IT Company WebPage Relaunch looking for modern and clean approach

We are looking to relaunch our website, to give it a more modern and clean look.
Company Background:
With nearly 20 years of industry expertise, we've been committed to delivering top-notch professional services and products, ensuring client success and efficiency. Our mission is to provide clients with talented human and technological resources, employing industry best practices for effective solutions. We envision becoming a pivotal player in Dominican Republic's Techonology sector, expanding our footprint across the Caribbean Central America and USA
Design Objectives:
1. Brand Identity: The website should reflect our brand identity based in our logo, color scheme, and overall aesthetic. Consistency with existing brand materials is essential.
2. User Experience: Prioritize user experience by ensuring easy navigation and intuitive layout. The website should be accessible and responsive across various devices and screen sizes.
3. Content Presentation: Present our content (text, images, videos) in a visually appealing and organized manner. Use creative layouts and typography to enhance readability and engagement.
4. Functionality: Implement necessary features and functionalities to support our business objectives. This may include contact form.
5. SEO Optimization: Design the website with search engine optimization (SEO) best practices in mind to improve visibility and ranking on search engine results pages (SERPs).
6. Multilanguage: Spanish and English
Pages and Sections:
1. Home Page:
o Welcome message/introduction
o Highlights of key products/services
o Clear navigation to other sections/pages
o Metrics (10 Satisfied customer) (Services provided in 5 countries) etc.
2. About Us:
o Company overview
o Mission, vision, and values
o Team/Staff profiles (tentative)
3. Products/Services:
o Our Partners
o Detailed descriptions of products/services offered
o Images/videos
4. Portfolio/Projects:
o Our Customers
o Case Studies
o Customer’s testimonials
5. Blog/News:
o Platform for sharing industry insights, updates, or company news
o Categories/tags for easy browsing
6. Contact Us:
o Contact form
o Company address, phone number, email
o Social media links
Design Preferences:
• Clean and modern design aesthetic
• Use of whitespace to enhance readability and visual appeal
• High-quality images and graphics
• Responsive to multiple devices
Technical Requirements:
• Compatibility with major web browsers (Chrome, Firefox, Safari, Edge)
• Compliance with web standards and best practices
Current Website:
https://www.corvantel.com.do
Note: The website should not be on Wordpress, we want an html/css website.

```html
<!DOCTYPE html>
<html lang="en">
<head>
<meta charset="utf-8">
<title>Corvantel – Products Services</title>
<link href="https://fonts.googleapis.com/css2?family=Poppins:wght@400;500;600;700;800&display=swap" rel="stylesheet">
<style>
:root{
  --orange:#f0561f;
  --orange-2:#f7931e;
  --ink:#1d1d1f;
  --text:#4a4a4a;
  --muted:#8a8a8a;
  --badge:#eceef1;
  --footer:#2a2a2c;
  --footer-line:#444447;
  --white:#ffffff;
  --green:#2fbf5f;
}
*{box-sizing:border-box;margin:0;padding:0}
html,body{width:1200px;height:3300px;overflow:hidden}
body{font-family:"Poppins",sans-serif;color:var(--ink);background:var(--white);position:relative}
.abs{position:absolute}

/* header */
.site-header{left:0;top:0;width:1200px;height:64px;border-bottom:1px solid #eee}
.brand{left:40px;top:14px;display:flex;align-items:center;gap:10px}
.brand-dot{width:30px;height:30px;border-radius:50%;background:linear-gradient(135deg,var(--orange),var(--orange-2))}
.brand-name{font-weight:800;font-size:22px;line-height:1;color:var(--ink);letter-spacing:.5px}
.brand-tag{font-size:8px;font-weight:500;color:var(--ink);letter-spacing:.4px;margin-top:3px}
.main-nav{right:40px;top:22px;display:flex;gap:30px;font-size:13px;font-weight:500}
.main-nav span.active{color:var(--orange)}

/* title + partners */
.page-title{left:0;width:1200px;top:140px;text-align:center;font-size:54px;font-weight:700;letter-spacing:-.5px}
.partners{left:120px;top:282px;display:flex;gap:36px}
.partner-badge{width:213px;height:80px;border-radius:8px;background:var(--badge)}
.carousel-dots{left:0;width:1200px;top:408px;display:flex;justify-content:center;gap:8px}
.carousel-dots i{width:10px;height:10px;border-radius:50%;background:var(--ink)}
.carousel-dots i.on{background:var(--orange)}

/* service rows */
.service-photo{width:400px;height:410px;border-radius:24px}
.photo-office{background:linear-gradient(160deg,#d9d3cb,#8a7d70 60%,#3e3a36)}
.photo-meeting{background:linear-gradient(160deg,#e6e1da,#6d6760 55%,#2c2c30)}
.photo-team{background:linear-gradient(160deg,#c8ccd2,#6e6a66 55%,#2c2a28)}
.photo-security{background:linear-gradient(160deg,#dbe4ee,#3d6fa4 55%,#0d2744)}
.service-text{width:440px}
.service-title{font-size:29px;font-weight:700;margin-bottom:16px;letter-spacing:-.3px}
.service-title .num{font-weight:500}
.service-body{font-size:12.5px;line-height:1.6;color:var(--text)}
.btn{display:inline-block;margin-top:26px;padding:11px 22px;border-radius:22px;background:linear-gradient(90deg,var(--orange),var(--orange-2));color:var(--white);font-size:11px;font-weight:700;letter-spacing:.6px}

/* cta */
.cta-mark{left:140px;top:2420px;display:flex;align-items:center;justify-content:center}
.cta-circle{width:340px;height:340px;border-radius:50%;background:linear-gradient(135deg,#e8391e,var(--orange-2))}
.cta-text{left:570px;top:2440px;width:520px}
.cta-title{font-size:38px;font-weight:700;line-height:1.22;color:#1e2230}

/* footer */
.footer-wave{left:0;top:2720px}
.newsletter-title{left:0;width:1200px;top:2842px;text-align:center;color:var(--white);font-size:20px;font-weight:600}
.newsletter-form{left:326px;top:2878px;width:548px;height:40px;border-radius:20px;background:var(--white);display:flex;align-items:center;padding-left:18px;gap:10px;font-size:12px;color:var(--muted)}
.newsletter-btn{position:absolute;right:4px;top:4px;height:32px;padding:0 26px;border-radius:16px;background:linear-gradient(90deg,var(--orange),var(--orange-2));color:var(--white);font-size:11px;font-weight:700;line-height:32px;letter-spacing:.5px}
.footer-brand{left:140px;top:3000px;display:flex;align-items:center;gap:10px;color:var(--white)}
.footer-brand .brand-name,.footer-brand .brand-tag{color:var(--white)}
.social{left:222px;top:3096px;display:flex;gap:12px}
.social i{width:28px;height:28px;border-radius:50%;border:1px solid #777}
.footer-col{top:2990px;color:var(--white)}
.footer-col h4{font-size:16px;font-weight:600;margin-bottom:14px}
.footer-col li{list-style:none;font-size:12px;color:#cfcfcf;margin-bottom:8px}
.contact-item{display:flex;gap:10px;margin-bottom:12px;align-items:flex-start}
.contact-item b{display:block;font-size:10px;color:var(--orange);font-weight:700;letter-spacing:.5px}
.contact-item span{font-size:11px;color:#cfcfcf}
.footer-rule{left:40px;top:3234px;width:1120px;height:1px;background:var(--footer-line)}
.copyright{left:0;width:1200px;top:3256px;text-align:center;font-size:11px;color:#bdbdbd}
.float-btn{right:26px;width:36px;height:36px;border-radius:50%}
</style>
</head>
<body>

<header class="abs site-header">
  <div class="abs brand">
    <div class="brand-dot"></div>
    <div><div class="brand-name">CORVANTEL</div><div class="brand-tag">IT CONSULTING AND SERVICES</div></div>
  </div>
  <nav class="abs main-nav">
    <span>About Us ⌄</span><span class="active">Products Services ⌄</span><span>Partners</span><span>Portfolio Projects ⌄</span><span>Blog News</span><span>Contact Us</span>
  </nav>
</header>

<h1 class="abs page-title">Products Services</h1>
<div class="abs partners">
  <div class="partner-badge" role="img" aria-label="Partner badge"></div>
  <div class="partner-badge" role="img" aria-label="Partner badge"></div>
  <div class="partner-badge" role="img" aria-label="Partner badge"></div>
  <div class="partner-badge" role="img" aria-label="Partner badge"></div>
</div>
<div class="abs carousel-dots"><i class="on"></i><i></i><i></i></div>

<!-- 01 -->
<div class="abs service-photo photo-office" style="left:140px;top:548px;border-top-left-radius:110px" role="img" aria-label="Photo of a developer working on a laptop in an office"></div>
<div class="abs service-text" style="left:606px;top:598px">
  <h2 class="service-title"><span class="num">01:</span> Software Factory</h2>
  <p class="service-body">We specialize in providing tailored software talent, ensuring that each developer or team we integrate into your project is perfectly aligned with your goals and company culture. Our professionals are experts in the latest technologies and agile methodologies, ensuring efficient and effective implementation of your software projects, from mobile applications to complex enterprise systems. With a deep understanding of each client's needs, we offer flexibility and scalability to fit any size project.</p>
  <span class="btn">READ MORE</span>
</div>

<!-- 02 -->
<div class="abs service-text" style="left:140px;top:1000px">
  <h2 class="service-title"><span class="num">02:</span> Service Management</h2>
  <p class="service-body">We redefine IT service management with solutions that combine cutting-edge technology and an exceptional user experience. We facilitate intuitive self-service and efficient service management, allowing users to resolve problems quickly and autonomously. With integration capabilities that allow us to automate processes to adapt to the specific needs of each organization.</p>
  <span class="btn">READ MORE</span>
</div>
<div class="abs service-photo photo-meeting" style="left:650px;top:1000px;border-top-right-radius:110px" role="img" aria-label="Photo of colleagues in a business meeting"></div>

<!-- 03 -->
<div class="abs service-photo photo-team" style="left:140px;top:1468px;border-top-left-radius:110px" role="img" aria-label="Photo of a team working together on laptops"></div>
<div class="abs service-text" style="left:606px;top:1498px">
  <h2 class="service-title"><span class="num">03:</span> Infrastructure</h2>
  <p class="service-body">We have a comprehensive portfolio of infrastructure management and monitoring solutions, designed for both cloud and on-premises environments. We offer full visibility and control over your IT infrastructure enabling real-time monitoring and proactive alerts that minimize downtime and maximize performance. Our flexible approach adapts to any scale and need, integrating seamlessly with existing systems to provide a cohesive and efficient solution. Whether you're migrating to the cloud or managing a complex data center, our portfolio ensures your business-critical infrastructure is optimized, secure, and ready for your operations.</p>
  <span class="btn">READ MORE</span>
</div>

<!-- 04 -->
<div class="abs service-text" style="left:140px;top:2010px">
  <h2 class="service-title"><span class="num">04:</span> Security</h2>
  <p class="service-body">We have leading strategic allies in the area of cybersecurity with their solid portfolio of integrated solutions that provide holistic security, aimed at protecting all areas of business infrastructure. We offer solutions for comprehensive defense against threats, optimizing detection and prevention through centralized management and real-time visibility, suitable for cloud, on-premises and mixed deployment models.</p>
  <span class="btn">READ MORE</span>
</div>
<div class="abs service-photo photo-security" style="left:650px;top:1940px;border-top-right-radius:200px" role="img" aria-label="Photo of hands on a laptop showing a security screen"></div>

<!-- CTA -->
<div class="abs cta-mark" role="img" aria-label="Corvantel brand mark">
  <div class="cta-circle"></div>
</div>
<div class="abs cta-text">
  <h2 class="cta-title">Discover Our Portfolio Leading Innovation Let's Build Together!</h2>
  <span class="btn">EXPLORE NOW</span>
</div>

<!-- footer -->
<svg class="abs footer-wave" width="1200" height="580" viewBox="0 0 1200 580">
  <path d="M0 80 C300 10 500 0 700 40 C900 80 1050 60 1200 0 L1200 580 L0 580 Z" fill="#2a2a2c"/>
</svg>
<div class="abs newsletter-title">Newsletter</div>
<div class="abs newsletter-form">
  <svg width="14" height="14" viewBox="0 0 14 14"><circle cx="7" cy="7" r="6" fill="none" stroke="#999" stroke-width="1.4"/><circle cx="7" cy="7" r="2.4" fill="none" stroke="#999" stroke-width="1.4"/></svg>
  Enter your email address
  <span class="newsletter-btn">SUBSCRIBE</span>
</div>

<div class="abs footer-brand">
  <div class="brand-dot"></div>
  <div><div class="brand-name">CORVANTEL</div><div class="brand-tag">IT CONSULTING AND SERVICES</div></div>
</div>
<div class="abs social"><i></i><i></i><i></i></div>

<div class="abs footer-col" style="left:480px">
  <h4>Quick Links</h4>
  <ul><li>Start</li><li>Solutions &amp; Services</li><li>Partners</li><li>About us</li></ul>
</div>
<div class="abs footer-col" style="left:680px">
  <h4>Information</h4>
  <ul><li>Privacy Policy</li><li>Disclaimer</li><li>Terms &amp; Condition</li><li>Site Map</li></ul>
</div>
<div class="abs footer-col" style="left:862px">
  <h4>Contact Us</h4>
  <div class="contact-item">
    <svg width="14" height="14" viewBox="0 0 14 14"><path d="M3 1 L5 1 L6 4 L4.5 5 C5.3 7 7 8.7 9 9.5 L10 8 L13 9 L13 11 C13 12 12 13 11 13 C5.5 12.5 1.5 8.5 1 3 C1 2 2 1 3 1Z" fill="var(--orange)"/></svg>
    <div><b>PHONE</b><span>809-555-0142</span></div>
  </div>
  <div class="contact-item">
    <svg width="14" height="14" viewBox="0 0 14 14"><rect x="1" y="3" width="12" height="8" rx="1" fill="none" stroke="var(--orange)" stroke-width="1.4"/><path d="M1 3 L7 8 L13 3" fill="none" stroke="var(--orange)" stroke-width="1.4"/></svg>
    <div><b>EMAIL</b><span>info@corvantel.com.do</span></div>
  </div>
  <div class="contact-item">
    <svg width="14" height="14" viewBox="0 0 14 14"><circle cx="7" cy="7" r="6" fill="none" stroke="var(--orange)" stroke-width="1.4"/><path d="M1 7 H13 M7 1 C4 4 4 10 7 13 M7 1 C10 4 10 10 7 13" fill="none" stroke="var(--orange)" stroke-width="1.2"/></svg>
    <div><b>WEBSITE</b><span>https://www.corvantel.com.do</span></div>
  </div>
</div>

<div class="abs footer-rule"></div>
<div class="abs copyright">© 2024 Corvantel. All rights reserved.</div>

<div class="abs float-btn" style="top:3158px;background:var(--green)"></div>
<div class="abs float-btn" style="top:3202px;background:var(--green)"></div>
<div class="abs float-btn" style="top:3246px;background:var(--orange-2)"></div>

</body>
</html>
```